Talbrin Business Cards

Front and back. Simon Kavelle MBA is the CEO of Talbrin Homes. Black white and grays. Logo and cool design.

Target Market(s)

Professional lenders and investors

Industry/Entity Type

Real estate developer. NO HOUSES OR ROOFS

Contact Information for Business Card

Logo, name and unique design. Front and back. Simon Kavelle MBA is the CEO of Talbrin Homes. Black white and grays. Logo and cool design.

Font styles to use
Sans Serif

Colors

Designer to choose only greyscale colors for use in the design.

Requirements
Must have
• Cool look. Not the same card I could design.
Nice to have
• Something memorable
Should not have
• Basic

```html
<!DOCTYPE html>
<html lang="en">
<head>
<meta charset="utf-8">
<title>Talbrin Homes Business Cards</title>
<link rel="stylesheet" href="https://fonts.googleapis.com/css2?family=Montserrat:wght@400;600;800&display=swap">
<style>
  :root {
    --backdrop-light: #2e2e2e;
    --backdrop-dark: #0c0c0c;
    --card: #121212;
    --card-edge: #1c1c1c;
    --ink: #ffffff;
    --ink-soft: #d9d9d9;
    --ink-muted: #8a8a8a;
    --rule: #6a6a6a;
    --tab: #a3a3a3;
  }
  * { margin: 0; padding: 0; box-sizing: border-box; }
  html, body { width: 1200px; height: 1200px; overflow: hidden; }
  body {
    background: radial-gradient(ellipse at 60% 30%, var(--backdrop-light), var(--backdrop-dark) 75%);
    font-family: "Montserrat", sans-serif;
    position: relative;
  }
  .card {
    position: absolute;
    left: 180px;
    width: 840px;
    height: 480px;
    background: var(--card);
    border: 1px solid var(--card-edge);
    box-shadow: 0 18px 40px rgba(0,0,0,0.6);
  }
  .card--back { top: 100px; }
  .card--front { top: 620px; }

  .wordmark {
    color: var(--ink);
    font-weight: 800;
    letter-spacing: -1px;
    line-height: 1;
    display: flex;
    align-items: center;
    gap: 16px;
  }
  .wordmark__dot {
    width: 16px; height: 16px; background: var(--ink);
  }
  .card--back .wordmark {
    position: absolute; top: 50%; left: 50%;
    transform: translate(-50%, -50%);
    font-size: 64px;
    color: var(--ink-soft);
    white-space: nowrap;
  }
  .card--front .wordmark {
    position: absolute; top: 70px; left: 60px;
    font-size: 62px;
    white-space: nowrap;
  }

  .divider {
    position: absolute; left: 60px; top: 250px;
    width: 460px; height: 1px; background: var(--rule);
  }
  .contact {
    position: absolute; left: 60px; top: 278px;
    list-style: none;
    font-size: 22px; color: var(--ink);
    line-height: 40px;
    letter-spacing: 1px;
  }
  .contact__label {
    display: inline-block; width: 44px; color: var(--ink-muted);
  }
  .name-tab {
    position: absolute; right: 60px; top: 270px;
    width: 360px; height: 46px;
  }
  .name-tab svg { position: absolute; inset: 0; }
  .name-tab__text {
    position: absolute; right: 14px; top: 6px;
    font-size: 26px; color: var(--ink); white-space: nowrap; font-weight: 400;
  }
  .name-tab__text strong { font-weight: 600; }
  .role {
    position: absolute; right: 74px; top: 330px;
    font-size: 20px; color: var(--ink-muted); letter-spacing: 0.5px;
  }
</style>
</head>
<body>
  <section class="card card--back" aria-label="Card back">
    <div class="wordmark"><span class="wordmark__dot"></span>Talbrin Homes</div>
  </section>

  <section class="card card--front" aria-label="Card front">
    <div class="wordmark"><span class="wordmark__dot"></span>Talbrin Homes</div>
    <div class="divider"></div>
    <ul class="contact">
      <li><span class="contact__label">P :</span>214-555-0148</li>
      <li><span class="contact__label">E :</span>Simon@talbrinhomes.com</li>
      <li><span class="contact__label">W :</span>www.talbrinhomes.com</li>
    </ul>
    <div class="name-tab">
      <svg width="360" height="46" viewBox="0 0 360 46" aria-hidden="true">
        <polygon points="36,0 360,0 360,46 0,46" fill="var(--tab)"/>
        <line x1="-200" y1="0" x2="36" y2="0" stroke="var(--rule)" stroke-width="1"/>
      </svg>
      <div class="name-tab__text">Simon <strong>Kavelle</strong> MBA</div>
    </div>
    <div class="role">CEO of Talbrin Homes</div>
  </section>
</body>
</html>
```